Business Association Needs Anti-Litter Poster

We are a business association that works to keep our business district clean and safe. We work very hard to keep our streets and parks clean. We are located in a very densely populated part of the city with residents from many parts of the world. We would like a unique poster that that appeals to a multicultural community and reminds residents not to litter. Our community is called City Heights and is located within San Diego, California, USA. Our organizational web site is www.ferngroveba-sample.org

Reason: I extended the deadline in order to provided enough time to get feedback from my committee on which design they like best for the campaign.

```html
<!DOCTYPE html>
<html lang="en">
<head>
<meta charset="utf-8">
<title>Do Not Litter – Fern Grove Business Association</title>
<link rel="stylesheet" href="https://fonts.googleapis.com/css2?family=Squada+One&display=swap">
<style>
  :root {
    --paper: #f1f1f0;
    --paper-shade: #e2e2e1;
    --ink: #111111;
    --orange: #e8821f;
    --red: #d0232b;
    --brown: #6f4a17;
  }
  * { margin: 0; padding: 0; box-sizing: border-box; }
  html, body {
    width: 954px;
    height: 1200px;
    overflow: hidden;
    background: var(--paper);
  }
  .poster {
    position: relative;
    width: 954px;
    height: 1200px;
    overflow: hidden;
    background: radial-gradient(ellipse at 50% 40%, var(--paper) 55%, var(--paper-shade) 100%);
    font-family: "Squada One", sans-serif;
    color: var(--ink);
  }
  .org-mark {
    position: absolute;
    top: 130px;
    left: 0;
    width: 100%;
    display: flex;
    justify-content: center;
    align-items: center;
    gap: 16px;
  }
  .org-mark__square {
    width: 50px;
    height: 50px;
    background: var(--orange);
  }
  .org-mark__name {
    font-size: 44px;
    line-height: 1.05;
    color: var(--brown);
    text-align: left;
    letter-spacing: 1px;
  }
  .tagline {
    position: absolute;
    top: 400px;
    left: 0;
    width: 100%;
    text-align: center;
    font-size: 62px;
    line-height: 62px;
    letter-spacing: 3px;
    text-transform: uppercase;
  }
  .headline { position: absolute; inset: 0; }
  .headline__letter {
    position: absolute;
    line-height: 1;
    text-transform: uppercase;
    transform-origin: center center;
  }
  .is-orange { color: var(--orange); }
  .is-red { color: var(--red); }
  .is-brown { color: var(--brown); }
</style>
</head>
<body>
<main class="poster">
  <header class="org-mark">
    <span class="org-mark__square"></span>
    <span class="org-mark__name">Fern Grove<br>Business Association</span>
  </header>

  <p class="tagline">Please let’s keep<br>San Diego’s international<br>marketplace clean</p>

  <h1 class="headline" aria-label="Do not litter">
    <span class="headline__letter is-orange" style="left:172px;top:630px;font-size:290px;transform:rotate(-2deg)">D</span>
    <span class="headline__letter is-orange" style="left:292px;top:705px;font-size:270px;transform:rotate(5deg)">o</span>
    <span class="headline__letter is-red" style="left:455px;top:640px;font-size:290px;transform:rotate(3deg)">N</span>
    <span class="headline__letter is-red" style="left:578px;top:720px;font-size:250px;transform:rotate(-6deg)">o</span>
    <span class="headline__letter is-red" style="left:712px;top:660px;font-size:270px;transform:rotate(-5deg)">T</span>

    <span class="headline__letter is-brown" style="left:72px;top:950px;font-size:300px;transform:rotate(-10deg)">L</span>
    <span class="headline__letter is-brown" style="left:232px;top:925px;font-size:290px;transform:rotate(-4deg)">I</span>
    <span class="headline__letter is-brown" style="left:296px;top:975px;font-size:270px;transform:rotate(8deg)">T</span>
    <span class="headline__letter is-brown" style="left:422px;top:915px;font-size:280px;transform:rotate(-5deg)">T</span>
    <span class="headline__letter is-brown" style="left:548px;top:975px;font-size:250px;transform:rotate(2deg)">E</span>
    <span class="headline__letter is-brown" style="left:690px;top:950px;font-size:300px;transform:rotate(-10deg)">R</span>
  </h1>
</main>
</body>
</html>
```